Splash page redesign - http://thebrightwaterhomeadvisors.com/

I would like to modify my website splash page to include my nestory reviews in a somewhat prominent way without making the landing page too busy. My earned media gets me a lot clients and it needs to be available and noticeable without being TOO much.
I also want to change the tag line of the web site from: OVER $100,000,000 IN CLOSED SHORT SALE TRANSACTIONS to : BECAUSE YOU NEED A SHORT SALE COMPANY, NOT JUST AN AGENT. And the second line to be replaced with: OVER $150,000,000 IN CLOSED SHORT SALES AND WE COVER ALL OF MARYLAND
I really need the Nestory reviews to stand out and be seen when the page loads and people dont have to scroll down. LOVE the opt in for the free ebook near the top as well
Industry/Entity Type
Real Estate
Number of Pages Required
2 page
Font styles to use
Requirements
Must have
- I really need the Nestory reviews to stand out and be seen when the page loads and people dont have to scroll down. LOVE the opt in for the free ebook near the top as well
Nice to have
- mentioned above

```html
<!DOCTYPE html>
<html lang="en">
<head>
<meta charset="utf-8">
<title>Brightwater Short Sale Group</title>
<link href="https://fonts.googleapis.com/css2?family=Ubuntu:wght@400;500;700&family=Open+Sans:wght@400;700&family=Crimson+Text:ital,wght@0,700;1,700&display=swap" rel="stylesheet">
<style>
:root{
  --red:#b5202b;
  --dark:#1f2226;
  --darker:#17191c;
  --white:#ffffff;
  --blue:#1c6fe0;
  --slate:#4f7482;
  --muted:#b9bcc0;
  --green:#2ecc40;
}
*{box-sizing:border-box;margin:0;padding:0}
html,body{width:814px;height:1200px;overflow:hidden}
body{position:relative;background:var(--white);font-family:'Ubuntu',sans-serif;color:var(--dark)}
.abs{position:absolute}

/* header */
.site-header{left:0;top:0;width:814px;height:84px;background:var(--dark);border-top:3px solid var(--red)}
.brand{top:28px;font-weight:700;font-size:12px;line-height:14px;color:var(--white);display:flex;align-items:center;gap:6px;white-space:nowrap}
.brand .dot{width:9px;height:9px;background:var(--red);flex:none}
.contact-line{right:90px;top:25px;font-size:10.5px;color:var(--white)}
.contact-line span{margin-left:8px}
.main-nav{right:90px;top:46px;display:flex;gap:15px;font-size:10.5px;color:var(--white)}
.main-nav .active{border-bottom:2px solid var(--red);padding-bottom:3px}

/* hero */
.hero{left:0;top:84px;width:814px;height:238px;background:linear-gradient(120deg,#6a4a3a 0%,#8c5f48 30%,#5d6b4a 60%,#a9b39a 100%)}
.hero-callout{left:492px;top:113px;width:322px;height:155px;background:rgba(235,228,215,.72);padding:18px 4px 0 57px}
.hero-callout p{font-family:'Crimson Text',serif;font-weight:700;font-size:19px;line-height:30px;letter-spacing:-.3px;color:var(--red);white-space:nowrap}
.hero-callout em{font-style:italic}

/* question tiles */
.tile{top:349px;width:195px;height:71px;background:var(--red);color:var(--white);text-align:center}
.tile .q{width:34px;height:34px;border:1.5px solid var(--white);margin:10px auto 0;font-size:25px;line-height:31px;font-weight:400}
.tile .label{font-size:8.5px;margin-top:8px;letter-spacing:.2px}

.tagline{left:0;top:444px;width:814px;text-align:center;color:var(--red);font-size:15.5px;line-height:21px}

/* panels */
.panel{top:507px;width:196px;height:235px}
.review{left:98px;background:var(--dark)}
.review-head{height:33px;background:var(--blue);color:var(--white);font-weight:700;font-size:13px;display:flex;align-items:center;justify-content:center;gap:6px}
.review-head .sq{width:10px;height:10px;background:var(--white)}
.agent-photo{left:6px;top:38px;width:58px;height:58px;border-radius:50%;background:radial-gradient(circle at 50% 40%,#8a7a70,#3e3835)}
.agent-name{left:71px;top:40px;font-size:13px;color:var(--white)}
.stars{display:flex;gap:3px;align-items:center}
.agent-stars{left:71px;top:59px;font-size:7px;color:#5aa6ff}
.agent-meta{left:71px;top:73px;font-size:6px;color:var(--white);line-height:7.5px}
.agent-meta .count{background:var(--red);padding:0 2px;margin-right:3px;font-size:5.5px}
.review-card{left:8px;width:180px;height:55px;border:1px solid #3a3d42;border-radius:2px;padding:4px 5px}
.review-card .top{display:flex;align-items:center;gap:5px;font-size:7.5px;color:var(--white)}
.review-card .who{font-size:6px;color:#5aa6ff;margin-top:2px}
.review-card .what{font-size:6.2px;color:var(--white);font-weight:500}
.review-card .body{font-size:5.2px;color:var(--muted);line-height:6px;margin-top:3px}

.video{left:310px;background:#050505}
.video-frame{left:0;top:29px;width:196px;height:176px;background:linear-gradient(160deg,#4f6f3a 0%,#6f8d55 30%,#4e5fa8 65%,#3b4a86 100%)}

.mission{left:521px;background:var(--slate);color:var(--white);padding:10px 12px}
.mission h3{font-family:'Open Sans',sans-serif;font-size:11.5px;line-height:14px}
.mission h2{font-family:'Open Sans',sans-serif;font-size:14.5px;line-height:19px;margin-bottom:6px}
.mission p{font-size:7.1px;line-height:8.4px;margin-bottom:8px}

/* news */
.news{left:0;top:774px;width:814px;height:102px;background:var(--dark)}
.news h2{position:absolute;left:98px;top:16px;color:var(--red);font-weight:400;font-size:15.5px}
.news-item{top:50px;display:flex;gap:12px}
.news-item .thumb{width:32px;height:32px;margin-top:1px;background:linear-gradient(135deg,#5a4636,#c9a37a)}
.news-item .date{font-size:7.5px;color:var(--red);font-weight:700}
.news-item .text{font-size:7.5px;color:var(--white);line-height:9px;margin-top:5px}

/* footer */
.footer{left:0;top:876px;width:814px;height:280px;background:var(--red);color:var(--white)}
.footer h2{position:absolute;top:20px;font-weight:400;font-size:16px}
.quick-links{left:102px;top:54px;list-style:none;font-size:7.5px;line-height:13px}
.quick-links li::before{content:"» ";}
.award-card{left:224px;top:56px;width:117px;height:172px;background:var(--white);border-radius:2px}
.address{left:398px;top:54px;font-size:7.3px;line-height:13px}
.field{left:558px;width:158px;height:25px;background:var(--white);font-size:8.5px;color:#b0b0b0;padding:7px 6px}
.submit{left:645px;top:1108px;width:71px;height:16px}
.submit span{display:block;margin:2px;height:12px;background:#111;color:var(--white);font-size:8.5px;text-align:center;line-height:12px;outline:1px solid #fff;outline-offset:1px}

.copyright{left:0;top:1156px;width:814px;height:44px;background:var(--dark);color:var(--white);font-size:7.5px;text-align:center;line-height:44px}
</style>
</head>
<body>

<header class="abs site-header">
  <div class="abs brand" style="left:98px">Harbor &amp; Key<br>Realty</div>
  <div class="abs brand" style="left:208px;top:35px"><span class="dot"></span>Brightwater</div>
  <div class="abs contact-line">Mail-info@harborkey.com <span>Phone-888-555-0142</span></div>
  <nav class="abs main-nav">
    <span class="active">Home</span><span>About us</span><span>Testimonial</span><span>Sortsale Ino</span><span>Contact Us</span>
  </nav>
</header>

<section class="abs hero" role="img" aria-label="Happy family celebrating in front of their brick home holding a sold sign"></section>
<div class="abs hero-callout"><p>Most times we market without<br>signs or lockboxes so most<br>people won’t know that your<br>home sold - <em>unless you tell them!</em></p></div>

<div class="abs tile" style="left:98px"><div class="q">?</div><div class="label">DO WE QUALIFY FOR SHORT SALE?</div></div>
<div class="abs tile" style="left:310px"><div class="q">?</div><div class="label">WHAT IS MY HOME WORTH?</div></div>
<div class="abs tile" style="left:521px"><div class="q">?</div><div class="label">COMMON MISCONCEPTION &amp; MISTAKES</div></div>

<div class="abs tagline">Because You Need a Short Sale Company, Not Merely a Realtor<br>Over $150,000,000 In Closed Short Sales And We Cover All Of Maryland</div>

<section class="abs panel review">
  <div class="review-head"><span class="sq"></span>Nestory Review</div>
  <div class="abs agent-photo" role="img" aria-label="Portrait of agent Dean Hollister"></div>
  <div class="abs agent-name">Dean Hollister</div>
  <div class="abs stars agent-stars">
    <svg width="52" height="8" viewBox="0 0 52 8"><g fill="#2ecc40"><polygon points="4,0 5,3 8,3 5.5,5 6.5,8 4,6 1.5,8 2.5,5 0,3 3,3"/><polygon transform="translate(11 0)" points="4,0 5,3 8,3 5.5,5 6.5,8 4,6 1.5,8 2.5,5 0,3 3,3"/><polygon transform="translate(22 0)" points="4,0 5,3 8,3 5.5,5 6.5,8 4,6 1.5,8 2.5,5 0,3 3,3"/><polygon transform="translate(33 0)" points="4,0 5,3 8,3 5.5,5 6.5,8 4,6 1.5,8 2.5,5 0,3 3,3"/><polygon transform="translate(44 0)" points="4,0 5,3 8,3 5.5,5 6.5,8 4,6 1.5,8 2.5,5 0,3 3,3"/></g></svg>
    (88 Review)
  </div>
  <div class="abs agent-meta"><div style="font-size:6.5px;margin-bottom:3px"><span class="count">651</span>Total Sales</div>Realtor (16 years experience)<br>Specialties: Listing Agent, Foreclosure,</div>

  <div class="abs review-card" style="top:108px">
    <div class="top"><svg width="62" height="10" viewBox="0 0 62 10"><g fill="#2ecc40"><polygon points="5,0 6.3,3.6 10,3.6 7,6 8.2,10 5,7.6 1.8,10 3,6 0,3.6 3.7,3.6"/><polygon transform="translate(13 0)" points="5,0 6.3,3.6 10,3.6 7,6 8.2,10 5,7.6 1.8,10 3,6 0,3.6 3.7,3.6"/><polygon transform="translate(26 0)" points="5,0 6.3,3.6 10,3.6 7,6 8.2,10 5,7.6 1.8,10 3,6 0,3.6 3.7,3.6"/><polygon transform="translate(39 0)" points="5,0 6.3,3.6 10,3.6 7,6 8.2,10 5,7.6 1.8,10 3,6 0,3.6 3.7,3.6"/><polygon transform="translate(52 0)" points="5,0 6.3,3.6 10,3.6 7,6 8.2,10 5,7.6 1.8,10 3,6 0,3.6 3.7,3.6"/></g></svg>Highly likely to recommend</div>
    <div class="who">mbreeze</div>
    <div class="what">Sold a Single Family home</div>
    <div class="body">Dean and his team were wonderful. We would highly recommend his services to</div>
  </div>
  <div class="abs review-card" style="top:170px">
    <div class="top"><svg width="62" height="10" viewBox="0 0 62 10"><g fill="#2ecc40"><polygon points="5,0 6.3,3.6 10,3.6 7,6 8.2,10 5,7.6 1.8,10 3,6 0,3.6 3.7,3.6"/><polygon transform="translate(13 0)" points="5,0 6.3,3.6 10,3.6 7,6 8.2,10 5,7.6 1.8,10 3,6 0,3.6 3.7,3.6"/><polygon transform="translate(26 0)" points="5,0 6.3,3.6 10,3.6 7,6 8.2,10 5,7.6 1.8,10 3,6 0,3.6 3.7,3.6"/><polygon transform="translate(39 0)" points="5,0 6.3,3.6 10,3.6 7,6 8.2,10 5,7.6 1.8,10 3,6 0,3.6 3.7,3.6"/><polygon transform="translate(52 0)" points="5,0 6.3,3.6 10,3.6 7,6 8.2,10 5,7.6 1.8,10 3,6 0,3.6 3.7,3.6"/></g></svg>Highly likely to recommend</div>
    <div class="who">mbreeze</div>
    <div class="what">Sold a Single Family home</div>
    <div class="body">Dean and his team were wonderful. We would highly recommend his services to</div>
  </div>
</section>

<section class="abs panel video">
  <svg class="abs" style="left:150px;top:8px" width="40" height="14" viewBox="0 0 40 14">
    <circle cx="7" cy="7" r="6" fill="#fff"/><path d="M7 3v4l3 2" stroke="#050505" stroke-width="1.4" fill="none"/>
    <path d="M24 11c1-4 4-6 9-6V2l5 5-5 5V8c-4 0-7 1-9 3z" fill="#fff"/>
  </svg>
  <div class="abs video-frame" role="img" aria-label="Video still of the agent speaking to camera"></div>
  <svg class="abs" style="left:42px;top:108px" width="14" height="14" viewBox="0 0 14 14"><polygon points="2,1 13,7 2,13" fill="#fff"/></svg>
</section>

<section class="abs panel mission">
  <h3>It’s Not Just Our Business,</h3>
  <h2>Its Our Mission</h2>
  <p>We are experts working with homeowners who owe more than their home is worth and no longer wish to keep the property but don’t want the Massive exposure/damage from just walking away.</p>
  <p>We have an exceptionally high success rate in having foreclosure auctions postponed and short sales closed (92%).</p>
  <p>Not only is our service no cost (we are paid by your lender) the majority of our clients actually receive seller incentives from their mortgage companies. These lender incentives range from $1,000 for FHA loans up to $60,000 on certain conventional mortgages. They are provided to assist with relocation.</p>
  <p>We experts in having the underwater portion</p>
</section>

<section class="abs news">
  <h2>Latst News</h2>
  <div class="abs news-item" style="left:98px"><div class="thumb" role="img" aria-label="News thumbnail"></div><div><div class="date">Jan 2 2017</div><div class="text">We have an excep-<br>tionally high success</div></div></div>
  <div class="abs news-item" style="left:267px"><div class="thumb" role="img" aria-label="News thumbnail"></div><div><div class="date">Jan 2 2017</div><div class="text">We have an excep-<br>tionally high success</div></div></div>
  <div class="abs news-item" style="left:436px"><div class="thumb" role="img" aria-label="News thumbnail"></div><div><div class="date">Jan 2 2017</div><div class="text">We have an excep-<br>tionally high success</div></div></div>
  <div class="abs news-item" style="left:600px"><div class="thumb" role="img" aria-label="News thumbnail"></div><div><div class="date">Jan 2 2017</div><div class="text">We have an excep-<br>tionally high success</div></div></div>
</section>

<footer class="abs footer">
  <h2 style="left:97px">Quick Links</h2>
  <h2 style="left:222px">Awards</h2>
  <h2 style="left:397px">Address</h2>
  <h2 style="left:554px">Quick Contact</h2>
  <ul class="abs quick-links">
    <li>Home</li><li>About us</li><li>Projects</li><li>Partner With Us</li><li>Career</li><li>Downloads</li><li>Contact</li>
  </ul>
  <div class="abs award-card">
    <svg width="117" height="172" viewBox="0 0 117 172">
      <rect x="28" y="14" width="60" height="50" rx="6" fill="#c9ccd0"/>
      <rect x="40" y="122" width="34" height="34" rx="6" fill="#1d3f7a"/>
    </svg>
  </div>
  <div class="abs address">Dean Hollister, Harbor &amp; Key Realty<br>The Coastal Short Sale Group<br>Phone: 888-555-0142<br>Fax: 866-555-0190<br><br>Email: dhollister@hkrealty.com</div>
</footer>
<div class="abs field" style="top:933px">Enter Your Name</div>
<div class="abs field" style="top:969px">Enter Your Email</div>
<div class="abs field" style="top:1004px">Enter Your Phone</div>
<div class="abs field" style="top:1040px;height:49px">Enter Your Message</div>
<div class="abs submit"><span>Submit</span></div>

<div class="abs copyright">Copyright © 2017 The Coastal Short Sale Group. All rights reserved.</div>
</body>
</html>
```